Property Development Business Cards

I need a business card design for Blue Harbour Developments Pty Ltd. We are a property development company in Australia and our name defines the five values that we adhere to, being Profitable, Partnerships, Quality Developments, Eco Friendly and Enduring Design.

I have attached the current logo that I use, it is just five yellow circles connected to a single cricle in the middle.

Target Market(s)

Our Target audience is real estate agents, owners of properties, builders and other trades

Industry/Entity Type

Business

Requirements
Must have
• Want to have two sides to the card, one with details and one to just highlight the company

```html
<!DOCTYPE html>
<html lang="en">
<head>
<meta charset="utf-8">
<title>Blue Harbour Developments – Business Cards</title>
<link href="https://fonts.googleapis.com/css2?family=Arimo:wght@400;700&display=swap" rel="stylesheet">
<style>
  :root {
    --brand-yellow: #edb42b;
    --ink: #4d4d4d;
    --ink-dark: #3a3a3a;
    --paper: #ffffff;
    --board: #ffffff;
    --board-edge: #9a9a9a;
    --crop: #000000;
  }
  * { box-sizing: border-box; margin: 0; padding: 0; }
  html, body {
    width: 1200px; height: 447px; overflow: hidden;
    background: var(--board);
    font-family: "Arimo", Arial, sans-serif;
  }
  .board {
    position: relative; width: 1200px; height: 447px;
    background: var(--board);
    box-shadow: inset 0 0 14px 4px var(--board-edge);
  }
  .card {
    position: absolute; top: 98px; width: 432px; height: 247px;
    background: var(--paper);
    box-shadow: 2px 3px 7px rgba(0,0,0,0.45);
    overflow: hidden;
  }
  .card--front { left: 99px; }
  .card--back { left: 664px; background: var(--brand-yellow); }

  .wordmark {
    position: absolute; left: 58px; top: 30px;
    display: flex; align-items: center; gap: 16px;
  }
  .wordmark__dot {
    width: 40px; height: 40px; border-radius: 50%;
    background: var(--brand-yellow);
  }
  .wordmark__name {
    color: var(--ink); font-weight: 700; font-size: 29px;
    line-height: 30px; letter-spacing: -0.5px;
  }
  .holder {
    position: absolute; left: 0; right: 0; top: 113px;
    text-align: center; color: var(--ink); font-weight: 700; font-size: 17px;
  }
  .contact {
    position: absolute; left: 0; right: 0; top: 152px;
    text-align: center; color: var(--ink); font-size: 13.5px; line-height: 21px;
  }
  .web-band {
    position: absolute; left: 0; right: 0; bottom: 0; height: 42px;
    display: flex; align-items: center; justify-content: center;
    font-weight: 700; font-size: 16px;
  }
  .card--front .web-band { background: var(--brand-yellow); color: var(--paper); }
  .card--back .web-band { background: var(--paper); color: var(--ink-dark); }

  .back-name {
    position: absolute; left: 212px; top: 108px;
    color: var(--paper); font-weight: 700; font-size: 23px; line-height: 24px;
    letter-spacing: -0.3px;
  }

  .crop { position: absolute; background: var(--crop); }
  .crop--v { width: 1px; height: 12px; }
  .crop--h { width: 12px; height: 1px; }
</style>
</head>
<body>
<main class="board">

  <!-- crop marks: front card -->
  <span class="crop crop--v" style="left:99px; top:76px"></span>
  <span class="crop crop--v" style="left:531px; top:76px"></span>
  <span class="crop crop--v" style="left:99px; top:355px"></span>
  <span class="crop crop--v" style="left:531px; top:355px"></span>
  <span class="crop crop--h" style="left:77px; top:98px"></span>
  <span class="crop crop--h" style="left:541px; top:98px"></span>
  <span class="crop crop--h" style="left:77px; top:345px"></span>
  <span class="crop crop--h" style="left:541px; top:345px"></span>

  <!-- crop marks: back card -->
  <span class="crop crop--v" style="left:664px; top:76px"></span>
  <span class="crop crop--v" style="left:1095px; top:76px"></span>
  <span class="crop crop--v" style="left:664px; top:355px"></span>
  <span class="crop crop--v" style="left:1095px; top:355px"></span>
  <span class="crop crop--h" style="left:642px; top:98px"></span>
  <span class="crop crop--h" style="left:1105px; top:98px"></span>
  <span class="crop crop--h" style="left:642px; top:345px"></span>
  <span class="crop crop--h" style="left:1105px; top:345px"></span>

  <section class="card card--front" aria-label="Card front">
    <div class="wordmark">
      <span class="wordmark__dot"></span>
      <span class="wordmark__name">Blue Harbour<br>Developments</span>
    </div>
    <p class="holder">Daniel Marsh</p>
    <p class="contact">
      0400 555 123 &nbsp;| Daniel@BlueHarbourDevelopments.com.au<br>
      PO Box 218 | Kingsford, ACT 2900
    </p>
    <div class="web-band">www.blueharbourdevelopments.com.au</div>
  </section>

  <section class="card card--back" aria-label="Card back">
    <p class="back-name">Blue Harbour<br>Developments</p>
    <div class="web-band">www.blueharbourdevelopments.com.au</div>
  </section>

</main>
</body>
</html>
```